Criação de Kit com 6 Layouts de Post para Redes Sociais (Facebook, Instagram e etc) + Capa de Facebook para Advocacia e Direito
A empresa queria:
" O escritório atua na área previdênciaria "

```html
<!DOCTYPE html>
<html lang="pt-BR">
<head>
<meta charset="UTF-8">
<title>Consultoria Jurídica – Post</title>
<link rel="stylesheet" href="https://fonts.googleapis.com/css2?family=Marcellus&family=Montserrat:wght@500&display=swap">
<style>
  :root {
    --gold: #b38b4d;
    --gold-light: #d2b07a;
    --ink: #2f2f2f;
    --paper: #fbfbfa;
    --paper-shade: #eef0f2;
    --photo-dark: #3b2f26;
    --photo-mid: #8a6f55;
    --photo-light: #d9d3cb;
  }
  * { margin: 0; padding: 0; box-sizing: border-box; }
  html, body { width: 1200px; height: 1200px; overflow: hidden; }
  body {
    position: relative;
    background: linear-gradient(120deg, var(--paper) 0%, var(--paper) 45%, var(--paper-shade) 100%);
    font-family: "Montserrat", sans-serif;
    color: var(--ink);
  }
  .brand {
    position: absolute; left: 100px; top: 160px;
    display: flex; align-items: center; gap: 20px;
  }
  .brand-mark {
    width: 76px; height: 76px; border-radius: 50%;
    border: 3px solid var(--gold);
  }
  .brand-name {
    font-family: "Marcellus", serif;
    font-size: 34px; line-height: 1.1; letter-spacing: 2px;
    color: var(--gold);
    text-transform: uppercase;
  }
  .headline {
    position: absolute; left: 100px; top: 325px;
    font-family: "Marcellus", serif;
    font-size: 64px; line-height: 89px; letter-spacing: 1px;
    color: var(--gold);
    text-transform: uppercase;
  }
  .cta {
    position: absolute; left: 100px; top: 800px;
    width: 328px; height: 68px;
    border: 2.5px solid var(--ink); border-radius: 34px;
    display: flex; align-items: center; justify-content: center;
    font-family: "Marcellus", serif; font-size: 30px; letter-spacing: 1.5px;
    color: var(--ink);
  }
  .cursor { position: absolute; left: 318px; top: 850px; width: 44px; height: 56px; }
  .phone {
    position: absolute; left: 100px; top: 1062px;
    width: 352px; height: 58px;
    border: 2.5px solid var(--ink); border-radius: 29px;
    display: flex; align-items: center; justify-content: center; gap: 12px;
    font-size: 25px; letter-spacing: 1.5px; color: var(--ink);
  }
  .phone svg { width: 26px; height: 26px; }
  .photo-frame { position: absolute; left: 0; top: 0; width: 1200px; height: 1200px; pointer-events: none; }
</style>
</head>
<body>
  <div class="brand">
    <div class="brand-mark"></div>
    <div class="brand-name">Marcelo Vidal<br>Advogados</div>
  </div>

  <h1 class="headline">Mais segurança<br>e comodidade<br>para uma boa<br>consultoria<br>jurídica</h1>

  <div class="cta">FAÇA JÁ A SUA</div>
  <svg class="cursor" viewBox="0 0 22 28" aria-hidden="true">
    <path d="M2 2 L2 22 L7 17 L11 26 L14 24.5 L10 16 L17 16 Z" fill="#fff" stroke="#2f2f2f" stroke-width="1.6" stroke-linejoin="round"/>
  </svg>

  <div class="phone">
    <svg viewBox="0 0 24 24" aria-hidden="true">
      <path d="M6.6 3.5 L9.2 3.5 L10.5 8 L8.6 9.6 C9.7 11.9 12.1 14.3 14.4 15.4 L16 13.5 L20.5 14.8 L20.5 17.4 C20.5 18.9 19.3 20.2 17.8 20 C10.5 19.2 4.8 13.5 4 6.2 C3.8 4.7 5.1 3.5 6.6 3.5 Z" fill="none" stroke="#2f2f2f" stroke-width="1.8" stroke-linejoin="round"/>
    </svg>
    <span>(00) 0 0000.0000</span>
  </div>

  <svg class="photo-frame" viewBox="0 0 1200 1200">
    <defs>
      <linearGradient id="photoTone" x1="0" y1="0" x2="1" y2="1">
        <stop offset="0" stop-color="var(--photo-dark)"/>
        <stop offset="0.45" stop-color="var(--photo-mid)"/>
        <stop offset="0.7" stop-color="var(--photo-light)"/>
        <stop offset="1" stop-color="var(--photo-mid)"/>
      </linearGradient>
    </defs>
    <path role="img" aria-label="Fotografia de advogado assinando contrato à mesa com balança da justiça e martelo"
          d="M1200 12 L950 12 A250 250 0 0 0 700 262 L700 900 A250 250 0 0 0 950 1150 L1200 1150 Z"
          fill="url(#photoTone)"/>
    <path d="M1200 -8 L940 -8 A262 262 0 0 0 678 254 L678 910 A262 262 0 0 0 940 1172 L1200 1172"
          fill="none" stroke="var(--gold-light)" stroke-width="3"/>
  </svg>
</body>
</html>
```